KPT Building And Maintenance

Need a very professional looking double sided Buisiness card with all my details phone number, name, email, license number.

Target Market(s)

construction industry

Industry/Entity Type

building

Contact Information for Business Card

Name Dale Whitcombe. Email Address Info@KPTBuilding.example.au mobile number 0452918730 licence number 871406D. web site

```html
<!DOCTYPE html>
<html lang="en">
<head>
<meta charset="utf-8">
<title>KPT Building And Maintenance – Business Card</title>
<link href="https://fonts.googleapis.com/css2?family=Montserrat:wght@400;600;700&display=swap" rel="stylesheet">
<style>
  :root {
    --backdrop: #3a3a3a;
    --card: #161616;
    --card-back: #121212;
    --accent: #2a9ad8;
    --text: #f2f2f2;
    --muted: #d6d6d6;
  }
  * { box-sizing: border-box; margin: 0; padding: 0; }
  html, body {
    width: 1200px; height: 801px; overflow: hidden;
    background: var(--backdrop);
    font-family: "Montserrat", sans-serif;
  }
  .stage {
    width: 1200px; height: 801px;
    display: flex; align-items: center; justify-content: center; gap: 40px;
  }
  .card {
    position: relative;
    width: 520px; height: 297px;
    background: var(--card);
    border-bottom: 3px solid var(--accent);
    border-right: 2px solid var(--accent);
    box-shadow: 0 14px 30px rgba(0,0,0,0.45);
    overflow: hidden;
  }
  .card-front { display: flex; align-items: center; }
  .brand-block {
    width: 48%;
    display: flex; justify-content: center; align-items: center;
  }
  .brand-name {
    color: var(--text);
    font-weight: 700; font-size: 30px; letter-spacing: 1px;
    line-height: 1.1; text-align: center; text-transform: uppercase;
  }
  .divider {
    width: 2px; height: 110px; background: var(--accent);
  }
  .contact-block { padding-left: 24px; }
  .person-name {
    color: var(--accent); font-weight: 700; font-size: 20px;
    text-transform: uppercase; letter-spacing: 0.5px;
  }
  .licence {
    color: var(--muted); font-size: 13px; margin: 3px 0 14px;
  }
  .contact-list { list-style: none; }
  .contact-item {
    display: flex; align-items: center; gap: 8px;
    color: var(--text); font-size: 12.5px; margin-bottom: 6px;
  }
  .contact-icon { width: 12px; height: 12px; flex: none; }
  .card-back { background: var(--card-back); }
  .pattern-area {
    position: absolute; inset: 0;
    background: linear-gradient(125deg, #0b0b0b 0%, #181818 45%, #262626 100%);
  }
  .back-name {
    position: absolute; right: 64px; bottom: 92px;
    color: var(--text); font-weight: 700; font-size: 26px; letter-spacing: 1px;
  }
</style>
</head>
<body>
<main class="stage">
  <section class="card card-front">
    <div class="brand-block">
      <p class="brand-name">KPT<br>Building</p>
    </div>
    <div class="divider"></div>
    <div class="contact-block">
      <h1 class="person-name">Dale Whitcombe</h1>
      <p class="licence">licence number 871406D</p>
      <ul class="contact-list">
        <li class="contact-item">
          <svg class="contact-icon" viewBox="0 0 12 12"><path d="M2.5 1 L4.5 1 L5.2 3.5 L4 4.5 Q5 7 7.5 8 L8.5 6.8 L11 7.5 L11 9.5 Q10.5 11 9 11 Q1 10 1 2.5 Q1 1 2.5 1Z" fill="var(--accent)"/></svg>
          0452918730
        </li>
        <li class="contact-item">
          <svg class="contact-icon" viewBox="0 0 12 12"><rect x="0.5" y="2.5" width="11" height="7" fill="var(--accent)"/><path d="M0.5 2.5 L6 6.5 L11.5 2.5" stroke="var(--card)" stroke-width="1" fill="none"/></svg>
          Info@KPTBuilding.example.au
        </li>
        <li class="contact-item">
          <svg class="contact-icon" viewBox="0 0 12 12"><circle cx="6" cy="6" r="5.5" fill="var(--accent)"/><path d="M0.5 6 H11.5 M6 0.5 Q3 6 6 11.5 M6 0.5 Q9 6 6 11.5" stroke="var(--card)" stroke-width="0.8" fill="none"/></svg>
          www.KPTBuilding.example.au
        </li>
      </ul>
    </div>
  </section>

  <section class="card card-back">
    <div class="pattern-area" role="img" aria-label="Repeating tone-on-tone brand pattern in dark grey gloss"></div>
    <p class="back-name">KPT</p>
  </section>
</main>
</body>
</html>
```